Canadian Christian Church needs design for new sermon series

A graphic design for our series and an invitation card to invite people to the series. Check design brief for more detailed information. Target audience: young families and young adults. Looking for a creative design that will get people's attention and create interest. See design brief for copy of design purchased for previous series.
Updates
entered Apr 4 incorrectly. Need a week to receive and review designs, and today is Apr 2/19. Thanks!
Target Market(s)
young families and young adults
Colors
Designer to choose colors to be used in the design.
Look and feel

```html
<!DOCTYPE html>
<html lang="en">
<head>
<meta charset="utf-8">
<title>Messy – Joining God in the Mess</title>
<link rel="stylesheet" href="https://fonts.googleapis.com/css2?family=Archivo+Black&family=Bowlby+One&family=Crimson+Pro:wght@500&display=swap">
<style>
  :root {
    --sky-top: #5a2a6e;
    --sky-red: #d8283a;
    --sky-orange: #f2602a;
    --sky-glow: #f78a4a;
    --horizon: #5c4a55;
    --rubble: #3a1f12;
    --rubble-deep: #1e0f08;
    --band: rgba(196, 112, 76, 0.72);
    --white: #ffffff;
    --mark: #f08a28;
  }
  * { margin: 0; padding: 0; box-sizing: border-box; }
  html, body { width: 1200px; height: 943px; overflow: hidden; background: #000; }
  .poster { position: relative; width: 1200px; height: 943px; overflow: hidden; }
  .scene {
    position: absolute; inset: 0;
    background: linear-gradient(180deg,
      var(--sky-top) 0%,
      var(--sky-red) 14%,
      var(--sky-orange) 32%,
      var(--sky-glow) 44%,
      var(--sky-orange) 52%,
      var(--horizon) 60%,
      var(--rubble) 70%,
      var(--rubble-deep) 100%);
  }
  .series-title {
    position: absolute; left: 85px; top: 66px; width: 1027px;
    display: flex; justify-content: space-between;
    font-family: "Archivo Black", sans-serif;
    font-size: 214px; line-height: 1; color: var(--white);
    opacity: 0.95;
  }
  .band {
    position: absolute; left: 0; top: 663px; width: 1200px; height: 171px;
    background: var(--band);
  }
  .tagline {
    position: absolute; left: 68px; top: 676px;
    font-family: "Bowlby One", sans-serif;
    font-size: 74px; line-height: 74px; color: var(--white);
    letter-spacing: 0;
  }
  .tagline span { display: block; white-space: nowrap; }
  .tagline .second { padding-left: 151px; }
  .church {
    position: absolute; left: 840px; top: 676px; width: 350px;
    text-align: center;
  }
  .church-dot {
    display: block; width: 108px; height: 108px; margin: 0 auto 6px;
    border-radius: 50%; background: var(--mark);
  }
  .church-name {
    font-family: "Crimson Pro", serif; font-weight: 500;
    font-size: 25px; line-height: 30px; color: var(--white); white-space: nowrap;
  }
</style>
</head>
<body>
  <main class="poster">
    <div class="scene" role="img" aria-label="Photograph of a fiery red and orange sunset sky over a heap of scrap and rubble, with a single hand reaching up out of the pile"></div>
    <h1 class="series-title"><span>M</span><span>E</span><span>S</span><span>S</span><span>Y</span></h1>
    <div class="band"></div>
    <h2 class="tagline"><span>JOINING GOD IN</span><span class="second">THE MESS</span></h2>
    <div class="church">
      <span class="church-dot"></span>
      <p class="church-name">Westbrook Park Family Church</p>
    </div>
  </main>
</body>
</html>
```